Creation of a Velmora Flyer design

As part of the cr% 26 # 233; ation of our soci% 26 # 233; t% 26 # 233 ;, we wish to cr% 26 # 233; er a flyer pr% 26 # 233; feeling our diff% 26 # 233; annuities% 26 # 233; s business advisory services% 26 # 233; foreign% 26 # 232; res who wish to develop their activities% 26 # 233; s in Switzerland. We want a double-sided flyer that presents% 26 # 233; society% 26 # 233; t% 26 # 233; d% 26 # 39; a c% 26 # 244; t% 26 # 233; and who presents% 26 # 233; benefits of the other. We have d% 26 # 233; j% 26 # 224; made a very basic provisional flyer to be able to present our activities. We put it to you as an example.

Target Market(s)

European companies% 26 # 233; internal% 26 # 233; res% 26 # 233; es by the market% 26 # 233; Swiss

Industry/Entity Type

Business Consultant

Colors

Designer to choose colors to be used in the design.

Requirements
Must have
• Company name and contact details
A field to detail the services
Nice to have
• Some% 26 # 233; l% 26 # 233; elements that recall Switzerland and some% 26 # 233; l% 26 # 233; elements that recall c% 26 # 244; t% 26 # 233; % 26quot; business% 26quot;

```html
<!DOCTYPE html>
<html lang="en">
<head>
<meta charset="utf-8">
<title>Velmora Flyer</title>
<link href="https://fonts.googleapis.com/css2?family=Jost:wght@300;400;500;700&display=swap" rel="stylesheet">
<style>
:root{
  --page-bg:#e4e4e4;
  --sky:#3d86c9;
  --sky-light:#8fc1e8;
  --panel:#b3c2d1;
  --navy:#063a52;
  --white:#ffffff;
  --ink:#1b2530;
}
*{margin:0;padding:0;box-sizing:border-box}
html,body{width:1200px;height:959px;overflow:hidden;background:var(--page-bg)}
body{font-family:'Jost',sans-serif;color:var(--ink)}
.flyer{position:absolute;left:270px;top:35px;width:660px;height:890px;background:var(--panel);overflow:hidden;box-shadow:0 6px 18px rgba(0,0,0,.18)}
.hero-photo{position:absolute;left:0;top:0;width:594px;height:410px;
  background:linear-gradient(180deg,#2f79c4 0%,#69a9dd 45%,#dfe7ee 62%,#8d8f96 78%,#6b5a45 100%);
  clip-path:polygon(0 0,100% 0,100% 76%,0 100%)}
.web-strip{position:absolute;left:594px;top:0;width:66px;height:268px;background:var(--white)}
.web-strip .url{position:absolute;left:20px;bottom:18px;transform:rotate(-90deg);transform-origin:left bottom;
  white-space:nowrap;font-size:16px;letter-spacing:2px;color:var(--navy);font-weight:400;width:0}
.bridge-photo{position:absolute;left:231px;top:345px;width:344px;height:132px;
  background:linear-gradient(180deg,#3d86c9 0%,#9cc6e6 55%,#8a7d72 80%,#ece9e6 100%);
  box-shadow:0 4px 10px rgba(0,0,0,.25);clip-path:polygon(0 10%,100% 0,100% 100%,0 92%)}
.frame{position:absolute;left:36px;top:48px;width:372px;height:702px;border:2px solid var(--white)}
.brand-tile{position:absolute;left:480px;top:73px;width:70px;height:70px;border-radius:14px;background:var(--white);
  display:flex;align-items:center;justify-content:center;font-size:13px;font-weight:500;color:var(--navy)}
.intro{position:absolute;left:50px;top:476px;width:345px;font-size:9.5px;line-height:13px;color:var(--ink)}
.services{position:absolute;top:540px;width:168px;list-style:none;font-size:9.5px;line-height:12.5px}
.services li{position:relative;padding-left:10px;margin-bottom:6px}
.services li::before{content:"•";position:absolute;left:0}
.services.col-a{left:50px}
.services.col-b{left:226px;width:172px}
.pitch{position:absolute;left:432px;top:566px;width:190px;font-size:19px;line-height:21px;font-weight:700;color:var(--white)}
.contact-cue{position:absolute;left:36px;top:760px;font-size:11px;font-weight:700;color:var(--white);letter-spacing:.5px}
.footer{position:absolute;left:0;top:784px;width:660px;height:106px;background:var(--navy);color:var(--white)}
.footer .mark{position:absolute;left:33px;top:28px;width:32px;height:32px;border-radius:7px;background:var(--white)}
.footer .name{position:absolute;left:80px;top:20px;font-size:30px;font-weight:300;letter-spacing:3px}
.footer .address{position:absolute;left:278px;top:22px;font-size:9.5px;line-height:12.5px}
</style>
</head>
<body>
<div class="flyer">
  <div class="hero-photo" role="img" aria-label="Photo of a snow-covered Alpine peak under a blue sky"></div>
  <div class="web-strip"><span class="url">www.velmora.ch</span></div>
  <div class="bridge-photo" role="img" aria-label="Photo of a suspension bridge between snowy mountain rocks with a Swiss flag"></div>
  <div class="frame"></div>
  <div class="brand-tile">Velmora</div>

  <p class="intro">Thanks to its personalized approach and tailor-made assistance, Velmora offers you the right support to develop your business activities and answers to all your questions about the swiss market. As a partner we assist you in finding market opportunities:</p>

  <ul class="services col-a">
    <li>By providing commercial contacts that match your target profiles;</li>
    <li>By listing the legal and regulatory requirements specific to the Swiss market (Switzerland is not an EU member State);</li>
    <li>By putting you in contact with private or public interlocutors in the context of an individual contact programme;</li>
    <li>By preparing a market study that measures the potential of your prodct or service;</li>
  </ul>
  <ul class="services col-b">
    <li>By adapting your marketing material (website, brochures, flyers, etc.) to the specific needs of the Swiss market and by translating it into German and/or French;</li>
    <li>By organizing a promotional event that is tailored to your needs;</li>
    <li>By representing you at trade show or fairs;</li>
    <li>By assuming the fiscal representation of your company;</li>
    <li>By offering you logistical and administrative support.</li>
  </ul>

  <p class="pitch">You are convinced of the potential of your product or service and you wish to focus on the Swiss market, or you want to expand your market share!</p>

  <p class="contact-cue">Contact us!</p>

  <div class="footer">
    <span class="mark"></span>
    <span class="name">VELMORA</span>
    <p class="address">Neuchatel Office:<br>Velmora Sarl, Rue des Tilleuls 4, 2017 Boudry (Neuchatel)<br>+41 (0)32 555 01 23 &nbsp;| info@velmora.ch</p>
  </div>
</div>
</body>
</html>
```